Business Card Design for Vintage Jazz

I am a vintage jazz band leader in New York City. My groups play the music of the 1920s, 1930s and 1940s. My website is morvainhale.com for more info on what I do.

I am looking for a two sided business card design that has the look and feel of a really nice business card from the 1930s. I need to convey with the design that my work has that vintage kind of class and style, but also conveys that we are fun and entertaining.

Most importantly it should make a bold staement. If Walt Pemberly had a card, what would it have looked like? I want a card that I feel confident will make an impact and will let people know that my work is te the top that NYC has to offer in vintage jazz..

Note that I have only decided to avoid the "committed payment" option as I have not used this service before. Assuming that I get quality work I will select a design from those presented.

Target Market(s)

people who want to hire my band for events, media, and new fans of the band

Industry/Entity Type

Performing Art

Contact Information for Business Card

Definitely a matte finish, possibly a sort of old style of paper with that brown tint? definitely a thick card.

Requirements
Must have
• FRONT
• My name: Tobias Merrow
• What I do: Bandleader, Guitarist, Vocalist, Songwriter
• Contact Details: morvainhale.com tobias@morvainhale.com 646-555-0184
• BACK
• My Social Media Links:
• facebook.morvainhale.com
• twitter, instagram, linkedin: morvainhale
• I'm also including a photo image I would like to use. The photo's background is not needed, and to be honest isn't really desireable. Just looking to use the image of me.
Nice to have
• I'm attaching which could be used as is, omitted from the card, or altered maybe with text going around the outside of the circle or in some other way. It may need some clean up to the edges of the lettering as we only use it for the website thumbnail.
• If there's space I'd like to include the text "join our mailing list for a free song download: freesong.morvainhale.com" If not perhaps just "Download a Free Song at: freesong.morvainhale.com - something to this end.
Should not have
• anything cartoony. Don't think retro 90s's vision of the swing era, think actual swing era!
• anything modern. Got to look old school
• Try to avoid dark backgrounds. Since we often play in bars and clubs where it is dar, a d
• avoid script fonts.

```html
<!DOCTYPE html>
<html lang="en">
<head>
<meta charset="utf-8">
<title>Tobias Merrow — Business Card</title>
<link rel="stylesheet" href="https://fonts.googleapis.com/css2?family=Archivo:wght@400;600;700&display=swap">
<style>
  :root {
    --page: #ece8e1;
    --card: #ffffff;
    --ink: #000000;
    --teal: #5ec4b1;
    --photo-tone: #8d8f8f;
    --paper-shadow: rgba(0,0,0,0.22);
  }
  * { margin: 0; padding: 0; box-sizing: border-box; }
  html, body {
    width: 1200px; height: 892px; overflow: hidden;
    background: var(--page);
    font-family: "Archivo", Arial, sans-serif;
  }
  .stage { position: relative; width: 1200px; height: 892px; }

  .card {
    position: absolute;
    background: var(--card);
    box-shadow: 0 6px 18px var(--paper-shadow);
  }

  /* Front */
  .card-front {
    left: 80px; top: 131px; width: 360px; height: 630px;
    padding: 9px;
  }
  .front-inner {
    width: 100%; height: 100%;
    display: flex; flex-direction: column;
  }
  .portrait {
    height: 62%;
    background:
      radial-gradient(ellipse 42% 60% at 55% 62%, var(--photo-tone) 0%, rgba(141,143,143,0.6) 45%, rgba(94,196,177,0) 75%),
      var(--teal);
  }
  .identity {
    flex: 1;
    background: var(--ink);
    color: var(--card);
    text-align: center;
    padding: 30px 20px 0;
  }
  .name { font-size: 36px; font-weight: 600; letter-spacing: 0.5px; line-height: 1.1; }
  .role-lead { font-size: 22px; font-weight: 600; margin-top: 4px; }
  .roles { font-size: 20px; font-weight: 600; margin-top: 2px; }
  .contact { list-style: none; margin-top: 22px; font-size: 19px; line-height: 1.25; }

  /* Back */
  .card-back {
    left: 500px; top: 266px; width: 630px; height: 360px;
    overflow: hidden;
  }
  .monogram {
    position: absolute; left: 40px; top: 34px;
    display: flex; align-items: center; gap: 18px;
  }
  .monogram-ring { width: 60px; height: 60px; border: 7px solid var(--ink); border-radius: 50%; }
  .monogram-name { font-size: 46px; font-weight: 700; color: var(--ink); }
  .handles {
    position: absolute; left: 40px; top: 180px;
    color: var(--ink);
  }
  .site { font-size: 34px; line-height: 1.3; display: flex; align-items: center; gap: 40px; }
  .handle-row { font-size: 34px; line-height: 1.3; display: flex; align-items: center; gap: 18px; margin-top: 10px; }
  .social { display: flex; gap: 14px; }
  .social-mark { width: 40px; height: 40px; background: var(--ink); }
</style>
</head>
<body>
<div class="stage">
  <article class="card card-front">
    <div class="front-inner">
      <div class="portrait" role="img" aria-label="Black and white photo of the bandleader tipping a straw boater hat, on a teal background"></div>
      <div class="identity">
        <h1 class="name">Tobias Merrow</h1>
        <p class="role-lead">Bandleader</p>
        <p class="roles">Guitarist, Vocalist, Songwriter</p>
        <ul class="contact">
          <li>646-555-0184</li>
          <li>morvainhale.com</li>
          <li>tobias@morvainhale.com</li>
        </ul>
      </div>
    </div>
  </article>

  <article class="card card-back">
    <div class="monogram">
      <span class="monogram-ring"></span>
      <span class="monogram-name">Tobias Merrow</span>
    </div>
    <div class="handles">
      <p class="site">morvainhale.com <span class="social-mark" aria-hidden="true"></span></p>
      <p class="handle-row">morvainhale
        <span class="social" aria-hidden="true">
          <span class="social-mark"></span>
          <span class="social-mark"></span>
          <span class="social-mark"></span>
        </span>
      </p>
    </div>
  </article>
</div>
</body>
</html>
```